Stylish High End Wedding Videography/Films Website (BDMR)

We need a modern and high-end website look for our wedding video and films business. We films weddings all over the United Kingdom and at European destinations so need something to reflect our work. The website should be visually stunning with images and videos being the focal point as this is what our services are;

I have uploads of some items I like and the features the site needs to have. These have been taken from other websites using standout features.

We need the following pages;

1 - Homepage
2 - Films Index Page
3 - Individual Films Page
4 - Prices / Collection Page
5 - Reviews
6 - Options
7 - About
8 - Contact
9 - Blog Index
10 - Blog Page

All pages must be consistent so have a similar style.

Pages on menu:
Films
Prices
Reviews
Options
About
Contact

We require a responsive look too. Over 90% of our visitors access the website via their mobile devices.

Please use the colours from our logo to incorporate into the website.

Target Market(s)

Wedding Couples

Industry/Entity Type

Wedding Photography

Number of Pages Required

5+ page

Font styles to use
Sans Serif
Script

Requirements
Must have
• The logo must be in the centre of the menu at the top.

Social icons at the bottom of the page.

Use only two fonts including Lore which is supplied
Nice to have
• Different video for each page on the top header. This will play behind the menu.

```html
<!DOCTYPE html>
<html lang="en">
<head>
<meta charset="utf-8">
<title>Bram Delmore Wedding Films</title>
<link rel="stylesheet" href="https://fonts.googleapis.com/css2?family=Montserrat:wght@200;300;400;600&family=Great+Vibes&display=swap">
<style>
:root{
  --gold:#a88d4e;
  --gold-soft:#c8b27a;
  --brown:#3f3430;
  --brown-mid:#4f423d;
  --cream:#f7f4ef;
  --cream-dark:#efebe5;
  --text:#3b3431;
  --muted:#a39a92;
  --white:#ffffff;
}
*{margin:0;padding:0;box-sizing:border-box}
html,body{width:1200px;height:3568px;overflow:hidden;background:var(--white)}
body{font-family:"Montserrat",sans-serif;color:var(--text);position:relative}
.abs{position:absolute}
.photo{position:absolute}

/* header */
.hero{left:0;top:0;width:1200px;height:547px;
  background:linear-gradient(180deg,#fbfaf8 0%,#f3eee6 38%,#c9b99c 52%,#6c5a43 68%,#3b3025 100%)}
.hero-line{left:0;width:1200px;border-top:1px dashed #b9b1a6}
.nav{top:50px;font-size:10px;font-weight:600;letter-spacing:.5px;color:var(--text)}
.nav a{color:inherit;text-decoration:none;position:absolute;white-space:nowrap}
.brand{left:500px;top:36px;width:200px;text-align:center;color:var(--gold);font-weight:400}
.brand-name{font-size:11px;letter-spacing:2.6px}
.brand-sub{font-size:6px;letter-spacing:2.6px;margin-top:4px}
.burger{left:1119px;top:50px;width:14px}
.burger span{display:block;height:2px;background:var(--text);margin-bottom:3px}
.hero-arrow{top:484px;color:var(--white);font-size:16px}
.dots{left:520px;top:484px;width:160px;display:flex;justify-content:space-between;color:var(--white);font-size:8px}

/* intro */
.intro{left:0;top:547px;width:1200px;height:309px;background:var(--cream)}
.intro-mark{left:597px;top:605px;width:6px;height:32px;background:var(--gold)}
.intro-quote{left:250px;top:655px;width:700px;text-align:center;font-family:"Great Vibes",cursive;font-size:33px;line-height:41px;color:var(--gold-soft)}
.intro-body{left:300px;top:758px;width:600px;text-align:center;font-size:11px;line-height:23px;color:var(--text)}

/* grid */
.film{width:399px;height:163px}
.play{width:14px;height:14px;border:1px solid var(--white);border-radius:50%}
.play::after{content:"";position:absolute;left:5px;top:3px;border-left:5px solid var(--white);border-top:3.5px solid transparent;border-bottom:3.5px solid transparent}

/* about */
.about-bg{left:400px;top:1347px;width:800px;height:534px;background:var(--cream)}
.section-title{width:1200px;left:0;text-align:center;font-weight:200;font-size:27px;letter-spacing:1px;color:#8a817a}
.title-rule{left:594px;width:12px;border-top:1px solid var(--gold)}
.about-haze{left:200px;top:1460px;width:300px;height:306px;background:linear-gradient(135deg,#ececec,#ffffff 60%,#f2f2f2)}
.about-photo{left:245px;top:1497px;width:348px;height:233px;box-shadow:0 4px 18px rgba(0,0,0,.18);
  background:linear-gradient(90deg,#d8d8d8 0%,#efefef 40%,#6d6d6d 62%,#cfcfcf 100%)}
.about-rule{left:570px;top:1613px;width:48px;border-top:1px solid #bdb6ad}
.about-text{left:668px;top:1553px;width:335px;font-size:11px;line-height:17.5px;color:var(--muted)}

/* quote band */
.band-left{left:0;top:1881px;width:600px;height:547px;background:linear-gradient(160deg,#54463f,#3f3430 70%,#4a3d37)}
.band-right{left:600px;top:1881px;width:600px;height:547px;background:linear-gradient(200deg,#9d8448,#b39b63 50%,#a8904f)}
.band-rule{left:569px;top:2040px;width:50px;border-top:1px solid #cfc4b4}
.band-quote{left:310px;top:2075px;width:580px;text-align:center;font-family:"Great Vibes",cursive;font-size:21px;line-height:24px;color:var(--white)}
.diamond-frame{left:527px;top:2355px;width:146px;height:146px}

/* style */
.style{left:0;top:2428px;width:1200px;height:566px;background:var(--cream)}
.style-col{top:2657px;width:279px;font-size:11px;line-height:20.3px;color:var(--muted);text-align:justify}
.btn{background:var(--gold);color:var(--white);font-size:7px;font-weight:600;letter-spacing:.6px;text-align:center}

/* sign-off */
.signoff{left:0;top:2994px;width:1200px;height:266px;background:var(--cream-dark)}
.sign-name{left:0;top:3120px;width:1200px;text-align:center;color:var(--gold);font-size:30px;letter-spacing:8px;font-weight:300}
.sign-sub{left:0;top:3213px;width:1200px;text-align:center;color:var(--gold);font-size:10px;letter-spacing:4px;font-weight:300}
.strip{top:3260px;width:150px;height:191px}

/* footer */
.footer{left:0;top:3451px;width:1200px;height:117px;background:var(--brown)}
.footer-text{left:0;top:3488px;width:1200px;text-align:center;color:#e7e0d6;font-size:8px;letter-spacing:.4px}
.socials{left:568px;top:3508px;width:64px;display:flex;gap:4px;justify-content:center}
.socials span{width:12px;height:12px;border:1px solid #d8cfc3;border-radius:2px}
</style>
</head>
<body>

<!-- header / hero -->
<div class="abs hero" role="img" aria-label="Couple walking hand in hand across golden hills at sunset, mountains behind"></div>
<div class="abs hero-line" style="top:8px"></div>
<div class="abs hero-line" style="top:540px"></div>
<nav class="abs nav" style="left:0;width:1200px">
  <a style="left:308px">FILMS</a>
  <a style="left:363px">PRICES</a>
  <a style="left:424px">REVIEWS</a>
  <a style="left:733px">OPTIONS</a>
  <a style="left:805px">ABOUT</a>
  <a style="left:866px">CONTACT</a>
</nav>
<div class="abs brand">
  <div class="brand-name">BRAM DELMORE</div>
  <div class="brand-sub">WEDDING FILMS</div>
</div>
<div class="abs burger"><span></span><span></span><span></span></div>
<div class="abs hero-arrow" style="left:200px">&#8592;</div>
<div class="abs hero-arrow" style="left:992px">&#8594;</div>
<div class="abs dots"><span>1</span><span>2</span><span>3</span><span>4</span><span>5</span><span>6</span><span>7</span></div>

<!-- intro -->
<section class="abs intro"></section>
<div class="abs intro-mark"></div>
<p class="abs intro-quote">Not just another pretty dress. Your wedding is a personal story that we are there to document.</p>
<p class="abs intro-body">We believe best results come from telling it like it is. The art happens in recognizing the moments when the setting, subject and mood are in sync andthe real story unfolds naturally, without being contrived</p>

<!-- film grid -->
<div class="photo film" style="left:0;top:856px;background:linear-gradient(180deg,#9fb8cf,#c9a17e)" role="img" aria-label="Couple standing on desert boulders"></div>
<div class="photo film" style="left:400px;top:856px;background:linear-gradient(180deg,#a8c0d8,#e9e4dc 55%,#5fb6c6)" role="img" aria-label="Couple kissing beside a modern house and pool"></div>
<div class="photo film" style="left:800px;top:856px;background:linear-gradient(180deg,#d7a7a0,#6f4e4a)" role="img" aria-label="Couple beside a vintage car at dusk"></div>
<div class="photo film" style="left:0;top:1020px;background:linear-gradient(180deg,#e6c9c0,#7b7a73)" role="img" aria-label="Couple embracing on a palm-lined road"></div>
<div class="photo film" style="left:400px;top:1020px;background:linear-gradient(135deg,#3a2c25,#d9b38b 55%,#2a1f1c)" role="img" aria-label="Laughing guest in sunglasses"></div>
<div class="photo film" style="left:800px;top:1020px;background:linear-gradient(180deg,#c9cbd0,#8c7d63)" role="img" aria-label="Couple among desert trees"></div>
<div class="photo film" style="left:0;top:1184px;background:linear-gradient(180deg,#bfc7d1,#27506b 55%,#1e3c54)" role="img" aria-label="Couple by a mountain lake"></div>
<div class="photo film" style="left:400px;top:1184px;background:linear-gradient(180deg,#6b5a47,#3b2f27)" role="img" aria-label="Couple walking through a forest"></div>
<div class="photo film" style="left:800px;top:1184px;background:linear-gradient(135deg,#4a4535,#2b2820)" role="img" aria-label="Couple close together in woodland light"></div>
<div class="abs" style="left:12px;top:868px;width:374px;height:140px;border:1px solid rgba(255,255,255,.8)"></div>
<div class="abs play" style="left:197px;top:931px"></div>
<div class="abs play" style="left:593px;top:931px"></div>
<div class="abs play" style="left:993px;top:931px"></div>
<div class="abs play" style="left:593px;top:1095px"></div>
<div class="abs play" style="left:993px;top:1095px"></div>
<div class="abs play" style="left:193px;top:1259px"></div>
<div class="abs play" style="left:993px;top:1259px"></div>

<!-- about -->
<section class="abs about-bg"></section>
<h2 class="abs section-title" style="top:1418px">CHI SONO</h2>
<div class="abs title-rule" style="top:1466px"></div>
<div class="abs about-haze" role="img" aria-label="Faded soft-focus background image"></div>
<div class="photo about-photo" role="img" aria-label="Black and white portrait of the filmmaker on a beach"></div>
<div class="abs about-rule"></div>
<p class="abs about-text">Lorem ipsum dolor sit amet, adipiscing elit, sed do eiusmod incididunt labore et dolore magna aliqua. Risus in hendrerit gravida rutrum quisque non tellus orci ac. At erat pellentesque adipiscing commodo elit. Leo a diam sollicitudin tempor accumsan in nisl nisi scelerisque eu ultrices vitae auctor.</p>

<!-- quote band -->
<div class="photo band-left" role="img" aria-label="Couple embracing beside large rocks, brown tint"></div>
<div class="photo band-right" role="img" aria-label="Bride in a forest clearing, gold tint"></div>
<div class="abs band-rule"></div>
<p class="abs band-quote">Lorem ipsum dolor sit amet, adipiscing elit, sed do eiusmod incididunt labore et dolore magna aliqua. Risus in hendrerit gravida rutrum quisque non tellus orci ac. At erat pellentesque adipiscing commodo elit. Leo a diam sollicitudin tempor accumsan in nisl nisi scelerisque eu ultrices vitae auctor. Viverra orci sagittis eu volutpat. Volutpat sed cras ornare arcu dui vivamus. Integer vitae justo eget magna fermentum iaculis eu. Erat nam at lectus urna. Ac tortor vitae purus faucibus ornare.</p>

<!-- style -->
<section class="abs style"></section>
<svg class="abs diamond-frame" viewBox="0 0 146 146" role="img" aria-label="Couple dancing, black and white, in a diamond frame">
  <polygon points="73,1 145,73 73,145 1,73" fill="#f7f4ef" stroke="#bdb3a6" stroke-width="1"/>
  <defs><linearGradient id="dg" x1="0" y1="0" x2="1" y2="1"><stop offset="0" stop-color="#d9d6d2"/><stop offset="1" stop-color="#3c3a38"/></linearGradient></defs>
  <polygon points="73,12 134,73 73,134 12,73" fill="url(#dg)"/>
</svg>
<h2 class="abs section-title" style="top:2583px">IL MIO STILE</h2>
<div class="abs title-rule" style="top:2631px"></div>
<p class="abs style-col" style="left:298px">Lorem ipsum dolor sit amet, adipiscing elit, sed do eiusmod incididunt labore et dolore magna aliqua. Risus in hendrerit gravida rutrum quisque non tellus orci ac. At erat pellentesque adipiscing commodo elit. Leo a diam sollicitudin tempor accumsan in nisl nisi scelerisque eu ultrices vitae auctor. Viverra orci sagittis eu volutpat. Volutpat sed cras ornare arcu dui vivamus. Integer vitae justo eget magna fermentum iaculis eu. Erat nam at lectus urna. Ac tortor vitae purus faucibus ornare.</p>
<p class="abs style-col" style="left:624px">Lorem ipsum dolor sit amet, adipiscing elit, sed do eiusmod incididunt labore et dolore magna aliqua. Risus in hendrerit gravida rutrum quisque non tellus orci ac. At erat pellentesque adipiscing commodo elit. Leo a diam sollicitudin tempor accumsan in nisl nisi scelerisque eu ultrices vitae auctor. Viverra orci sagittis eu volutpat. Volutpat sed cras ornare arcu dui vivamus. Integer vitae justo eget magna fermentum iaculis eu. Erat nam at lectus urna. Ac tortor vitae purus faucibus ornare.</p>
<div class="abs btn" style="left:540px;top:2891px;width:118px;height:28px;line-height:28px">LEARN MORE</div>

<!-- sign-off -->
<section class="abs signoff"></section>
<div class="abs sign-name">BRAM DELMORE</div>
<div class="abs sign-sub">WEDDING FILMS</div>

<div class="photo strip" style="left:0;background:linear-gradient(180deg,#5d5753,#e6e4e1)" role="img" aria-label="Couple in front of a draped window, black and white"></div>
<div class="photo strip" style="left:150px;background:linear-gradient(180deg,#1f1d1c,#6b6864)" role="img" aria-label="Couple with sparklers at night"></div>
<div class="photo strip" style="left:300px;background:linear-gradient(180deg,#2c2a28,#8e8a85)" role="img" aria-label="Couple dancing in a reception hall"></div>
<div class="photo strip" style="left:450px;background:linear-gradient(180deg,#4a4643,#9a958f)" role="img" aria-label="Couple kissing close up"></div>
<div class="photo strip" style="left:600px;background:linear-gradient(180deg,#d8d6d2,#4a4745)" role="img" aria-label="Bride laughing with guest"></div>
<div class="photo strip" style="left:750px;background:linear-gradient(180deg,#3a3735,#c9c6c2)" role="img" aria-label="Bride twirling in her dress"></div>
<div class="photo strip" style="left:900px;background:linear-gradient(180deg,#b8b5b1,#55524f)" role="img" aria-label="Couple holding hands detail"></div>
<div class="photo strip" style="left:1050px;background:linear-gradient(180deg,#e3e1de,#6a6764)" role="img" aria-label="Couple smiling outdoors"></div>
<div class="abs btn" style="left:540px;top:3345px;width:120px;height:27px;line-height:27px">MORE DETAIL</div>

<!-- footer -->
<footer class="abs footer"></footer>
<svg class="abs" style="left:585px;top:3437px" width="30" height="30" viewBox="0 0 30 30">
  <polygon points="15,1 29,15 15,29 1,15" fill="#3f3430" stroke="#8a7d70" stroke-width="1"/>
</svg>
<p class="abs footer-text">© COPYRIGHT 2020 &nbsp; // &nbsp; TERMS AND POLICY &nbsp; // &nbsp; BRAM DELMORE WEDDING FILMS</p>
<div class="abs socials"><span></span><span></span><span></span><span></span></div>

</body>
</html>
```